PACKAGING AND LABEL DESIGN FOR LUXURY WHISKY BRAND

We need a label and packaging design for a new luxury whisky brand based in Singapore called Morvane. We need a label design and a suggested packaging design in a box/bag or wrap form. For the bottle it is fixed, so we would like suggestions to make the bottle like a piece of art. Please refer to Harlow whisky, Kelpa Rum, PLR and Vireo coffee for the inspiration and styles we like. For the words 1746 and Oat Whisky please make original fonts or artwork. We would like it to be in Serif font but we are open to suggestions
The bottle is as attached with the following dimensions
Height :159mm
Diammeter:84mm
Outter Diameter of mouth:39mm

We develop the world's first soy wines and spirits. Our new product is a soy based whisky that pays tribute to tradition and culture in Singapore while showcasing our nation's innovative and courageous spirit, moving from a swamp to a first world nation.

Please read the brand guidelines for deeper understanding

Target Market(s)

Global travellers coming to Singapore. Adventurous, innovators and independent self made pride.

Industry/Entity Type

Alcohol beverages

Requirements
Must have
• Original label design a box/packaging design, logo of morvane, logo of 1746, fonts and art of the labels
Nice to have
• Original artwork for 1746 and Oat Whisky. Batik prints, gold, soy beans/flowers, Singapore elements.
Should not have
• No copied work.

```html
<!DOCTYPE html>
<html lang="en">
<head>
<meta charset="utf-8">
<title>Morvane 1746 Oat Whiskey — Box and Label</title>
<link rel="stylesheet" href="https://fonts.googleapis.com/css2?family=Big+Shoulders+Display:wght@700;800;900&family=Cinzel:wght@700&family=Montserrat:wght@400&display=swap">
<style>
  :root {
    --stage: #17121a;
    --stage-glow: #231a20;
    --ink: #0b0b0b;
    --ink-soft: #1d1d1d;
    --edge: #2c2c2c;
    --side-light: #3a3a3a;
    --gold: #c9a24e;
    --gold-light: #e8c97c;
    --gold-deep: #8f6e2c;
    --cream: #f3efe6;
    --seal: #e9e4d6;
  }
  html, body {
    margin: 0;
    padding: 0;
    width: 1200px;
    height: 1196px;
    overflow: hidden;
    background: var(--stage);
  }
  .canvas {
    display: block;
    width: 1200px;
    height: 1196px;
    background: radial-gradient(ellipse at 50% 50%, var(--stage-glow) 0%, var(--stage) 70%);
  }
  .label-body { fill: var(--ink); stroke: var(--edge); stroke-width: 5; }
  .frame-outer { fill: none; stroke: var(--gold); stroke-width: 5; }
  .frame-chain { fill: none; stroke: var(--cream); stroke-width: 3; stroke-dasharray: 6 4; }
  .frame-inner { fill: none; stroke: var(--gold); stroke-width: 3; }
  .ribbon { fill: var(--ink); stroke: var(--gold); stroke-width: 2; }
  .logo-ring { fill: none; stroke: var(--gold); stroke-width: 9; }
  .box-front { fill: var(--ink); }
  .box-trim { stroke: var(--gold); stroke-width: 3; }
  .neck-seal { fill: var(--seal); }
  .seal-tag { fill: var(--ink); stroke: var(--gold); stroke-width: 2.5; }
  .origin {
    font-family: "Cinzel", serif;
    font-weight: 700;
    font-size: 14px;
    letter-spacing: 1.5px;
    fill: var(--cream);
  }
  .brand-name {
    font-family: "Montserrat", sans-serif;
    font-weight: 400;
    font-size: 50px;
    letter-spacing: 12px;
    fill: var(--gold);
  }
  .vintage {
    font-family: "Big Shoulders Display", sans-serif;
    font-weight: 800;
    font-size: 104px;
    fill: var(--cream);
  }
  .spec {
    font-family: "Big Shoulders Display", sans-serif;
    font-weight: 700;
    font-size: 28px;
    fill: var(--cream);
  }
  .spirit-name {
    font-family: "Big Shoulders Display", sans-serif;
    font-weight: 800;
    font-size: 42px;
    letter-spacing: 2px;
    fill: var(--cream);
  }
  .seal-text {
    font-family: "Big Shoulders Display", sans-serif;
    font-weight: 800;
    font-size: 24px;
    letter-spacing: 2px;
    fill: var(--ink);
  }
</style>
</head>
<body>
<svg class="canvas" viewBox="0 0 1200 1196" xmlns="http://www.w3.org/2000/svg">
  <defs>
    <linearGradient id="goldLeaf" x1="0" y1="0" x2="1" y2="1">
      <stop offset="0" stop-color="var(--gold-light)"/>
      <stop offset="0.5" stop-color="var(--gold)"/>
      <stop offset="1" stop-color="var(--gold-deep)"/>
    </linearGradient>
    <radialGradient id="batikField" cx="0.5" cy="0.5" r="0.6">
      <stop offset="0" stop-color="var(--ink-soft)"/>
      <stop offset="1" stop-color="var(--ink)"/>
    </radialGradient>
    <linearGradient id="sideBatik" x1="0" y1="0" x2="1" y2="1">
      <stop offset="0" stop-color="var(--side-light)"/>
      <stop offset="1" stop-color="var(--ink)"/>
    </linearGradient>
    <path id="originArc" d="M175,172 A230 230 0 0 1 385,172"/>
    <path id="spiritArc" d="M120,728 Q280,838 440,728"/>

    <symbol id="whiskyLabel" viewBox="0 0 560 960">
      <path class="label-body" d="M20,110 Q20,70 90,70 L170,70 Q200,10 280,10 Q360,10 390,70 L470,70 Q540,70 540,110 L540,850 Q540,890 470,890 L390,890 Q360,950 280,950 Q200,950 170,890 L90,890 Q20,890 20,850 Z"/>
      <path class="crest" role="img" aria-label="Gold filigree crest ornament" d="M180,78 Q230,20 280,22 Q330,20 380,78 Q330,62 280,66 Q230,62 180,78 Z" fill="url(#goldLeaf)" opacity="0.8"/>
      <path class="crest" role="img" aria-label="Gold filigree crest ornament" d="M180,882 Q230,940 280,938 Q330,940 380,882 Q330,898 280,894 Q230,898 180,882 Z" fill="url(#goldLeaf)" opacity="0.8"/>
      <g class="corner-panels" role="img" aria-label="Gold hatched corner filigree" fill="url(#goldLeaf)" opacity="0.4">
        <path d="M34,90 L150,90 Q70,120 52,230 L34,230 Z"/>
        <path d="M526,90 L410,90 Q490,120 508,230 L526,230 Z"/>
        <path d="M34,870 L150,870 Q70,840 52,730 L34,730 Z"/>
        <path d="M526,870 L410,870 Q490,840 508,730 L526,730 Z"/>
      </g>
      <rect class="batik-field" role="img" aria-label="Dark batik floral pattern" x="54" y="119" width="452" height="717" rx="226" fill="url(#batikField)"/>
      <rect class="frame-outer" x="30" y="95" width="500" height="765" rx="250"/>
      <rect class="frame-chain" x="42" y="107" width="476" height="741" rx="238"/>
      <rect class="frame-inner" x="54" y="119" width="452" height="717" rx="226"/>
      <path class="ribbon" d="M165,180 A240 240 0 0 1 395,180 L398,198 A240 240 0 0 0 162,198 Z"/>
      <text class="origin" text-anchor="middle"><textPath href="#originArc" startOffset="50%">FROM SINGAPORE</textPath></text>
      <circle class="logo-ring" cx="280" cy="325" r="105"/>
      <text class="brand-name" x="286" y="540" text-anchor="middle">MORVANE</text>
      <path class="scroll-ornament" role="img" aria-label="Gold scroll ornament" d="M220,610 Q250,572 280,570 Q310,572 340,610 Q310,598 280,598 Q250,598 220,610 Z" fill="url(#goldLeaf)"/>
      <text class="spec" x="128" y="668" text-anchor="middle">70cl e</text>
      <text class="vintage" x="280" y="690" text-anchor="middle" textLength="170" lengthAdjust="spacingAndGlyphs">1746</text>
      <text class="spec" x="430" y="668" text-anchor="middle">40%Vol</text>
      <path class="scroll-ornament" role="img" aria-label="Gold scroll ornament" d="M232,702 Q256,726 280,728 Q304,726 328,702 Q304,712 280,712 Q256,712 232,702 Z" fill="url(#goldLeaf)"/>
      <text class="spirit-name" text-anchor="middle"><textPath href="#spiritArc" startOffset="50%">OAT WHISKEY</textPath></text>
    </symbol>
  </defs>

  <!-- gift box -->
  <g class="gift-box">
    <rect class="box-side" role="img" aria-label="Black and grey batik floral print on box side" x="102" y="185" width="125" height="805" fill="url(#sideBatik)"/>
    <line class="box-trim" x1="102" y1="240" x2="227" y2="218"/>
    <line class="box-trim" x1="102" y1="905" x2="227" y2="950"/>
    <rect class="box-front" x="227" y="170" width="443" height="820"/>
    <line class="box-trim" x1="227" y1="218" x2="670" y2="228"/>
    <line class="box-trim" x1="227" y1="950" x2="670" y2="935"/>
    <use href="#whiskyLabel" x="274" y="285" width="350" height="600"/>
  </g>

  <!-- bottle label set -->
  <g class="bottle-dress">
    <rect class="neck-seal" x="835" y="265" width="44" height="112"/>
    <text class="seal-text" transform="translate(865 321) rotate(90)" text-anchor="middle">1746 1746</text>
    <circle class="seal-tag" cx="857" cy="390" r="26"/>
    <use href="#whiskyLabel" x="720" y="458" width="310" height="531"/>
  </g>
</svg>
</body>
</html>
```